Pain Seminar Flyer 8.5x11

We are having a FREE seminar on Pain for our Bootcamp members at our gym. We are looking for a great looking flyer with pictures and a design to draw people in. I have attached our logo, pictures of the 2 speakers and a Word document of the flyer information needed. PLEASE PLEASE make our head shots small and in a circle like the example flyer we attached but obviously make the flyer much much nicer than the example. Also we attached pic ideas about pain.
- This must be in PSD. format WITH LAYERS and fonts so we can edit the time or reuse the flyer.
- Size 8.5x11
- Attached info. with pics and logo (along with other pics of pain!)
Thank you!
Gym

```html
<!DOCTYPE html>
<html lang="en">
<head>
<meta charset="utf-8">
<title>Free Seminar on How to Stop Pain</title>
<link rel="stylesheet" href="https://fonts.googleapis.com/css2?family=Stardos+Stencil:wght@700&family=Oswald:wght@400;500&family=Montserrat:wght@500;700&display=swap">
<style>
  :root {
    --page-bg: #d9d6d1;
    --paper: #efefed;
    --brand-blue: #2e6fb0;
    --accent-amber: #b5731f;
    --ink: #151515;
    --band-dark: #2b2c2e;
    --caption-bg: rgba(30,30,30,0.85);
    --white: #ffffff;
  }
  * { box-sizing: border-box; margin: 0; padding: 0; }
  html, body { width: 960px; height: 1200px; overflow: hidden; }
  body { background: var(--page-bg); position: relative; }

  .flyer {
    position: absolute; left: 30px; top: 17px;
    width: 900px; height: 1165px;
    background: var(--paper);
    overflow: hidden;
    box-shadow: 0 2px 10px rgba(0,0,0,0.2);
  }
  .top-band { position: absolute; left: 0; top: 0; width: 900px; height: 142px; background: var(--brand-blue); }
  .bottom-band { position: absolute; left: 0; top: 1024px; width: 900px; height: 141px; background: var(--band-dark); }

  .pain-card {
    position: absolute; top: 50px; width: 260px; height: 175px;
    border: 4px solid var(--white); border-radius: 10px; overflow: hidden;
  }
  .pain-card .photo { position: absolute; inset: 0; }
  .pain-card .caption {
    position: absolute; left: 0; right: 0; bottom: 0; height: 45px;
    background: var(--caption-bg); color: var(--white);
    font: 400 27px/45px "Oswald", sans-serif; text-align: center;
    transform-origin: center; letter-spacing: -0.5px;
  }
  .card-back { left: 39px; } .card-shoulder { left: 316px; } .card-knee { left: 593px; }

  .headline { position: absolute; left: 0; top: 270px; width: 900px; height: 180px; }
  .headline text { font-family: "Stardos Stencil", serif; font-weight: 700; }

  .rule { position: absolute; left: 52px; width: 798px; height: 2px; background: var(--ink); }
  .rule-top { top: 476px; } .rule-mid { top: 553px; }
  .rule-date { left: 519px; width: 331px; top: 780px; height: 1px; }

  .condensed { font-family: "Oswald", sans-serif; font-weight: 400; color: var(--ink); position: absolute; letter-spacing: -0.6px; }
  .reservations { top: 489px; left: 0; width: 900px; text-align: center; font-size: 38px; line-height: 48px; }
  .reservations .call { color: var(--brand-blue); font-weight: 500; }
  .limited { top: 566px; left: 0; width: 900px; text-align: center; font-size: 33px; line-height: 46px; }

  .topics { position: absolute; left: 60px; top: 664px; list-style: none; }
  .topics li { display: flex; align-items: center; height: 50px; font: 400 28px/1 "Oswald", sans-serif; color: var(--ink); letter-spacing: -0.5px; }
  .topics svg { width: 22px; height: 22px; margin-right: 12px; }

  .event-date { position: absolute; left: 519px; top: 661px; color: var(--brand-blue); font: 500 38px/50px "Oswald", sans-serif; letter-spacing: -1px; }
  .venue { position: absolute; left: 517px; top: 798px; font: 400 22px/30px "Oswald", sans-serif; color: var(--ink); letter-spacing: -0.4px; }

  .speaker { position: absolute; width: 200px; text-align: center; top: 905px; }
  .speaker .portrait {
    width: 164px; height: 164px; border-radius: 50%; margin: 0 auto;
    border: 5px solid var(--white);
  }
  .speaker .name { margin-top: 21px; font: 700 22px/26px "Montserrat", sans-serif; color: var(--white); }
  .speaker .creds { font: 500 15px/20px "Montserrat", sans-serif; color: var(--white); }
  .speaker-1 { left: 36px; } .speaker-2 { left: 231px; }
  .speaker-1 .portrait { background: linear-gradient(160deg, #8a8a6e, #c9b59a 60%, #d8cbb6); }
  .speaker-2 .portrait { background: linear-gradient(160deg, #b9b3ac, #c48e6c 60%, #9a6a4d); }

  .brand-box {
    position: absolute; left: 517px; top: 961px; width: 328px; height: 109px;
    background: var(--white); border: 5px solid var(--ink); border-radius: 6px;
    display: flex; align-items: center; justify-content: center; gap: 12px;
  }
  .brand-box .mark { width: 18px; height: 18px; background: var(--brand-blue); }
  .brand-box .brand-name { font: 500 34px/1 "Oswald", sans-serif; color: var(--brand-blue); letter-spacing: 0.5px; text-transform: uppercase; }
  .website { position: absolute; left: 517px; width: 328px; top: 1099px; text-align: center; font: 700 22px/28px "Montserrat", sans-serif; color: var(--accent-amber); }
</style>
</head>
<body>
<main class="flyer">
  <div class="top-band"></div>
  <div class="bottom-band"></div>

  <figure class="pain-card card-back">
    <div class="photo" role="img" aria-label="Photo of a man holding his sore upper back" style="background: radial-gradient(circle at 55% 45%, #d0452e, #a0573a 40%, #5a3a2b 80%);"></div>
    <figcaption class="caption">BACK PAIN?</figcaption>
  </figure>
  <figure class="pain-card card-shoulder">
    <div class="photo" role="img" aria-label="Photo of a man holding his sore shoulder" style="background: radial-gradient(circle at 25% 35%, #e0402a, #a0583a 35%, #4e3226 80%);"></div>
    <figcaption class="caption">SHOULDER PAIN?</figcaption>
  </figure>
  <figure class="pain-card card-knee">
    <div class="photo" role="img" aria-label="Photo of a man holding his sore knee" style="background: radial-gradient(circle at 75% 40%, #e0402a, #8a5236 35%, #1f1a18 75%);"></div>
    <figcaption class="caption">KNEE PAIN?</figcaption>
  </figure>

  <svg class="headline" viewBox="0 0 900 180" aria-label="Free seminar on how to stop pain">
    <text x="54" y="96" font-size="100" fill="var(--brand-blue)" textLength="793" lengthAdjust="spacingAndGlyphs">FREE SEMINAR</text>
    <text x="52" y="162" font-size="66" fill="var(--accent-amber)" textLength="795" lengthAdjust="spacingAndGlyphs">ON HOW TO STOP PAIN</text>
  </svg>

  <div class="rule rule-top"></div>
  <p class="condensed reservations">RESERVATIONS REQUIRED. <span class="call">CALL 303-555-0147 TODAY</span></p>
  <div class="rule rule-mid"></div>
  <p class="condensed limited">LIMITED SPACE SO DON’T WAIT TO SIGN UP</p>

  <ul class="topics">
    <li><svg viewBox="0 0 22 22"><rect x="2" y="4" width="15" height="15" fill="none" stroke="var(--accent-amber)" stroke-width="2"/><path d="M5 11l4 4 10-12" fill="none" stroke="var(--accent-amber)" stroke-width="2.2"/></svg>How to Get Out of Pain</li>
    <li><svg viewBox="0 0 22 22"><rect x="2" y="4" width="15" height="15" fill="none" stroke="var(--accent-amber)" stroke-width="2"/><path d="M5 11l4 4 10-12" fill="none" stroke="var(--accent-amber)" stroke-width="2.2"/></svg>What to do When an Exercise Hurts</li>
    <li><svg viewBox="0 0 22 22"><rect x="2" y="4" width="15" height="15" fill="none" stroke="var(--accent-amber)" stroke-width="2"/><path d="M5 11l4 4 10-12" fill="none" stroke="var(--accent-amber)" stroke-width="2.2"/></svg>How Exercise Helps Pain</li>
    <li><svg viewBox="0 0 22 22"><rect x="2" y="4" width="15" height="15" fill="none" stroke="var(--accent-amber)" stroke-width="2"/><path d="M5 11l4 4 10-12" fill="none" stroke="var(--accent-amber)" stroke-width="2.2"/></svg>Q &amp; A to Fine Extraordinary Health</li>
  </ul>

  <p class="event-date">THURSDAY APRIL 13th<br>7:30PM-9PM</p>
  <div class="rule rule-date"></div>
  <p class="venue">COREVIA PERSONAL TRAINING STUDIO<br>118 Elm St. Westbrook, CO 80999</p>

  <div class="speaker speaker-1">
    <div class="portrait" role="img" aria-label="Head shot of speaker Daniel Marsh"></div>
    <p class="name">Daniel Marsh</p>
    <p class="creds">PT, DPT, OCS</p>
  </div>
  <div class="speaker speaker-2">
    <div class="portrait" role="img" aria-label="Head shot of speaker Colin Hart"></div>
    <p class="name">Colin Hart</p>
    <p class="creds">MS, CSCS, FMS</p>
  </div>

  <div class="brand-box">
    <span class="mark"></span>
    <span class="brand-name">Corevia Bootcamps</span>
  </div>
  <p class="website">www.coreviafit.com</p>
</main>
</body>
</html>
```